Summer Sunglass offer

Need a poster design for a spring / summer campaign. We are an opticians with good footfall. The design needs to be eye catching and aimed at 40 year old plus. The offer is Up to 50% off sunglass offer, t&c apply. (I have attached our last year campaign)
Also need a 2 sided A5 leaflet design (see attached)
I've uploaded a copy of our logo

A5 leaflet should read:

Grab a bargain on two great looks this summer Upto 50% off sunglasses
Look great and stay safe in the sun this summer

We want you to look great, feel fantastic and most of all stay safe in the sun this summer. That’s why we’re offering you 50% off prescription sunglasses with every complete pair of glasses you buy this summer or 25% off for prescription sunglasses with no other purchase.
Find you new summer looks from our gorgeous collection of frames in store. It matters to us that you look great in your new glasses as much as how well you see through them, so we’ll be on hand to help you find frames that suit you best.
What new looks will you go for? Smart or sassy? Formal or Fun? Whatever you’re in the mood for, you’ll find it in our collections this summer.
Call in today to find your new looks, and remember to bring your prescription if you don’t need an eye test.

Target Market(s)

40 + year old

Industry/Entity Type

Optician

Colors

Designer to choose colors to be used in the design.

Requirements
Must have
• Images, preferably a male and Female image

```html
<!DOCTYPE html>
<html lang="en">
<head>
<meta charset="utf-8">
<title>Summer Sunglass Offer – A5 Leaflet</title>
<link href="https://fonts.googleapis.com/css2?family=Cormorant+Garamond:wght@500&family=Oswald:wght@500&family=Ubuntu:wght@300;400&display=swap" rel="stylesheet">
<style>
  :root {
    --bg: #e6e6e6;
    --paper: #ffffff;
    --paper-soft: #f3f3f3;
    --teal: #5aabb0;
    --teal-light: #a9d9dd;
    --ink: #3d3d3d;
    --ink-soft: #4a4a4a;
    --brand: #3a8f98;
    --gold: #d8b27a;
    --bar: #8c8c8f;
    --white: #ffffff;
  }
  * { box-sizing: border-box; margin: 0; padding: 0; }
  html, body { width: 1200px; height: 871px; overflow: hidden; background: var(--bg); }
  .canvas { position: relative; width: 1200px; height: 871px; }

  .leaflet {
    position: absolute; width: 492px; height: 698px;
    background: var(--paper); overflow: hidden;
    box-shadow: 0 3px 10px rgba(0,0,0,.18);
  }
  .leaflet--front { left: 66px; top: 80px; }
  .leaflet--back { left: 607px; top: 78px; background: var(--paper-soft); }

  .photo { position: absolute; }
  .leaflet--front .photo {
    left: 70px; top: 0; width: 422px; height: 610px;
    background: linear-gradient(90deg, rgba(255,255,255,0) 0%, #d9d6d2 18%, #cfcac4 45%, #e9e7e4 70%, #bdb8b2 100%);
    -webkit-mask-image: linear-gradient(180deg, #000 88%, transparent 100%);
    mask-image: linear-gradient(180deg, #000 88%, transparent 100%);
  }
  .leaflet--back .photo {
    left: 60px; top: 0; width: 432px; height: 218px;
    background: linear-gradient(90deg, rgba(255,255,255,0) 0%, #efe6dc 20%, #d9bfa4 55%, #c7a07a 80%, #e4cfb6 100%);
  }

  .frame { position: absolute; }
  .leaflet--front .frame { left: 184px; top: 21px; width: 261px; height: 557px; border: 4px solid var(--gold); }
  .leaflet--back .frame { left: 79px; top: 18px; width: 394px; height: 183px; border: 3px solid var(--white); }

  .badge { position: absolute; width: 130px; height: 130px; }
  .leaflet--front .badge { left: 72px; top: 222px; }
  .leaflet--back .badge { left: 27px; top: 52px; }
  .badge svg { position: absolute; inset: 0; }
  .badge__text {
    position: absolute; inset: 0; display: flex; flex-direction: column;
    align-items: center; justify-content: center;
    font-family: "Oswald", sans-serif; font-weight: 500; color: var(--ink);
    line-height: 1.05; text-transform: uppercase;
  }
  .badge__small { font-size: 17px; }
  .badge__big { font-size: 29px; }

  .headline-band {
    position: absolute; left: 26px; width: 466px; height: 115px;
    background: var(--teal); color: var(--white); text-align: center;
    padding-top: 18px;
  }
  .leaflet--front .headline-band { top: 381px; }
  .leaflet--back .headline-band { top: 218px; }
  .headline-band h1 {
    font-family: "Cormorant Garamond", serif; font-weight: 500;
    font-size: 27px; line-height: 31px; letter-spacing: 3px; text-transform: uppercase;
  }
  .headline-band p {
    font-family: "Ubuntu", sans-serif; font-weight: 300; font-size: 12.5px; margin-top: 7px;
  }

  .body-copy {
    position: absolute; left: 26px; top: 346px; width: 446px;
    font-family: "Ubuntu", sans-serif; font-weight: 300; font-size: 12.4px;
    line-height: 14.2px; color: var(--ink-soft); text-align: justify;
  }
  .body-copy p + p { margin-top: 14px; }
  .body-copy p.tight { margin-top: 0; }

  .brand {
    position: absolute; left: 0; width: 100%;
    display: flex; align-items: center; justify-content: center; gap: 9px;
    font-family: "Ubuntu", sans-serif; font-weight: 400; color: var(--brand);
  }
  .leaflet--front .brand { top: 621px; }
  .leaflet--back .brand { top: 562px; }
  .brand__dot { width: 30px; height: 30px; border-radius: 50%; background: var(--brand); }
  .brand__name { font-size: 19px; line-height: 19px; letter-spacing: 1px; text-transform: uppercase; }
  .brand__name small { display: block; font-size: 10px; letter-spacing: 3.6px; margin-top: 3px; }

  .contact-bar {
    position: absolute; left: 0; top: 621px; width: 100%; height: 34px;
    background: var(--bar); color: var(--white);
    font-family: "Ubuntu", sans-serif; font-size: 9.6px;
    display: flex; align-items: center; justify-content: center; gap: 18px;
  }
  .contact-bar span, .web { display: flex; align-items: center; gap: 6px; }

  .web {
    position: absolute; left: 0; width: 100%; justify-content: center;
    font-family: "Ubuntu", sans-serif; font-weight: 300; font-size: 13px; color: var(--ink-soft);
  }
  .leaflet--front .web { top: 671px; }
  .leaflet--back .web { top: 673px; }
</style>
</head>
<body>
<div class="canvas">

  <!-- Front side -->
  <section class="leaflet leaflet--front">
    <div class="photo" role="img" aria-label="Photo of a woman in a white outfit wearing large sunglasses on a city street"></div>
    <div class="frame"></div>
    <div class="badge">
      <svg viewBox="0 0 130 130" aria-hidden="true">
        <circle cx="68" cy="63" r="56" fill="var(--teal-light)" opacity=".85"/>
        <circle cx="62" cy="66" r="58" fill="none" stroke="var(--gold)" stroke-width="1"/>
        <circle cx="66" cy="64" r="61" fill="none" stroke="var(--gold)" stroke-width=".7" opacity=".7"/>
      </svg>
      <div class="badge__text">
        <span class="badge__small">Upto</span>
        <span class="badge__big">50% off</span>
        <span class="badge__small">Sunglasses</span>
      </div>
    </div>
    <div class="headline-band">
      <h1>Grab a bargain on two<br>great looks this summer</h1>
      <p>Look great and stay safe in the sun this summer</p>
    </div>
    <div class="brand">
      <div class="brand__dot"></div>
      <div class="brand__name">Hollowford<small>Eyecare Centre</small></div>
    </div>
    <div class="web">
      <svg width="12" height="12" viewBox="0 0 12 12" aria-hidden="true"><circle cx="6" cy="6" r="5" fill="none" stroke="#777" stroke-width="1.2"/><path d="M1 6h10M6 1c-2.5 3-2.5 7 0 10M6 1c2.5 3 2.5 7 0 10" fill="none" stroke="#777" stroke-width="1"/></svg>
      hollowfordeyecare.co.uk
    </div>
  </section>

  <!-- Back side -->
  <section class="leaflet leaflet--back">
    <div class="photo" role="img" aria-label="Photo of a smiling couple wearing sunglasses in summer sunshine"></div>
    <div class="frame"></div>
    <div class="badge">
      <svg viewBox="0 0 130 130" aria-hidden="true">
        <circle cx="68" cy="63" r="56" fill="var(--teal-light)" opacity=".85"/>
        <circle cx="62" cy="66" r="58" fill="none" stroke="var(--gold)" stroke-width="1"/>
        <circle cx="66" cy="64" r="61" fill="none" stroke="var(--gold)" stroke-width=".7" opacity=".7"/>
      </svg>
      <div class="badge__text">
        <span class="badge__small">Upto</span>
        <span class="badge__big">50% off</span>
        <span class="badge__small">Sunglasses</span>
      </div>
    </div>
    <div class="headline-band">
      <h1>Grab a bargain on two<br>great looks this summer</h1>
      <p>Look great and stay safe in the sun this summer</p>
    </div>
    <div class="body-copy">
      <p>We want you to look great, feel fantastic and most of all stay safe in the sun this summer. That’s why we’re offering you 50% off prescription sunglasses with every complete pair of glasses you buy this summer or 25% off for prescription sunglasses with no other purchase.</p>
      <p>Find you new summer looks from our gorgeous collection of frames in store. It matters to us that you love how you look in your new glasses as much as how well you see through them, so we’ll be on hand to help you find frames that suit you best.</p>
      <p>What new looks will you go for? Smart or sassy? Formal or Fun? Whatever you’re in the mood for, you’ll find it in our collections this summer.</p>
      <p class="tight">Call in today to find your new looks, and remember to bring your prescription if you don’t need an eye test.</p>
    </div>
    <div class="brand">
      <div class="brand__dot"></div>
      <div class="brand__name">Hollowford<small>Eyecare Centre</small></div>
    </div>
    <div class="contact-bar">
      <span>
        <svg width="9" height="12" viewBox="0 0 9 12" aria-hidden="true"><path d="M4.5 0A4.5 4.5 0 0 0 0 4.5C0 8 4.5 12 4.5 12S9 8 9 4.5A4.5 4.5 0 0 0 4.5 0zm0 6.3a1.8 1.8 0 1 1 0-3.6 1.8 1.8 0 0 1 0 3.6z" fill="#fff"/></svg>
        48 Market Road, Hollowford, Kent HF2 7QL
      </span>
      <span>
        <svg width="11" height="11" viewBox="0 0 11 11" aria-hidden="true"><path d="M2.2 0.5l1.7 2.3-1 1.2c.7 1.5 1.8 2.6 3.3 3.3l1.2-1 2.3 1.7-.8 2c-4.8-.3-8.3-3.8-8.6-8.6z" fill="#fff"/></svg>
        Book your appointment or call us on 01632 960418
      </span>
    </div>
    <div class="web">
      <svg width="12" height="12" viewBox="0 0 12 12" aria-hidden="true"><circle cx="6" cy="6" r="5" fill="none" stroke="#777" stroke-width="1.2"/><path d="M1 6h10M6 1c-2.5 3-2.5 7 0 10M6 1c2.5 3 2.5 7 0 10" fill="none" stroke="#777" stroke-width="1"/></svg>
      hollowfordeyecare.co.uk
    </div>
  </section>

</div>
</body>
</html>
```